Start-up company developing economical and ecological hydrogen peroxide generator needs an attractiv

We need a powerpoint design for a start-up company based in Montreal called Vorbelle currently seeking to raise funds from investors. We develop an electrochemical hydrogen peroxide generator based on new generation catalysts.

These generators allow industrial users of hydrogen peroxide to generate it onsite economically and ecologically, as opposed to buying it from the major suppliers who make it large production plants using more polluting methods and need to transport it to customers over long distances.

We would like to see designs that have a cleantech technology and green chemistry feel. Colors that evoke a sense of environmental sustainability are desired.

The final design should communicate technological innovation that makes the world a cleaner and healthier place to live.

Target Market(s)

Industrial users or producers of of hydrogen peroxide

Industry/Entity Type

It Company

Font styles to use
Sans Serif

Colors
0255a3
3276b5
85acd3
9bcb3b
add136
e3eebf

Requirements
Must have
• Clean, attractive, professional and advanced technology look.
• Our slogan is: Catalyst for innovation
Nice to have
• The cover page should have our logo and our slogan. It should also have some graphics that pertain to technology and green chemistry. The perception that one should have when looking at it is that the company is developing a clean chemical manufacturing technology that is more environmentally friendly.
• Each other template page should have our logo discretely included in it.
• Other than the cover page, the template pages should not be too crowded with design elements. There should be lots of clear space to add material.
• I have uploaded some inspirational images that can be used to help come up with some designs.

```html
<!DOCTYPE html>
<html lang="en">
<head>
<meta charset="utf-8">
<title>Vorbelle — Presentation Template</title>
<link href="https://fonts.googleapis.com/css2?family=Lato:ital,wght@0,300;0,400;0,700;1,300;1,400&display=swap" rel="stylesheet">
<style>
:root{
  --blue-dark:#0255a3;
  --blue:#3276b5;
  --blue-light:#85acd3;
  --green:#9bcb3b;
  --green-bright:#add136;
  --green-pale:#e3eebf;
  --frame:#a7b0b8;
  --ink:#333a44;
  --grey:#7b8593;
  --logo-grey:#8d95a3;
  --paper:#f4f6fa;
  --band:#dfe5ee;
}
*{box-sizing:border-box;margin:0;padding:0}
html,body{width:1063px;height:1200px;overflow:hidden}
body{background:var(--frame);font-family:'Lato',sans-serif;position:relative;color:var(--ink)}
.slide{position:absolute;width:516px;height:386px;overflow:hidden;
  background:linear-gradient(180deg,#f7f8fb 0%,#f1f4f9 60%,#e3e9f2 100%)}
.s1{left:12px;top:11px}.s2{left:538px;top:11px}
.s3{left:12px;top:406px}.s4{left:538px;top:406px}
.s5{left:12px;top:802px}.s6{left:538px;top:802px}
.abs{position:absolute}
.center{left:0;right:0;text-align:center}
.wordmark{font-family:'Lato',sans-serif;font-weight:400;letter-spacing:1px}
.slogan{font-style:italic;font-weight:300;color:var(--blue-light);font-size:30px}

/* content slides */
.head{position:absolute;left:0;right:0;top:0;height:46px;background:#fafbfd;border-bottom:1px solid var(--green-pale)}
.head h2{position:absolute;left:0;right:0;top:8px;text-align:center;font-weight:400;font-size:25px;line-height:1;color:var(--blue-dark)}
.head p{position:absolute;left:0;right:0;top:34px;text-align:center;font-size:8px;color:var(--grey);text-transform:uppercase}
.head p b{font-weight:700}
.head.muted h2{color:#7a8494}
.foot{position:absolute;left:0;right:0;bottom:0;height:31px;background:var(--band);display:flex;align-items:center;font-size:9px;color:var(--grey)}
.foot .mark{margin-left:12px;width:60px;font-size:11px;font-style:normal;color:var(--logo-grey)}
.foot .line{margin-left:10px}
.foot .line b{font-weight:700}
.foot .num{margin-left:auto;margin-right:22px}
.foot.blue{background:var(--blue);color:#fff}
.foot.blue .mark{color:#fff}
.placeholder{position:absolute;background:#eef1f5;border:1px solid var(--green-pale)}
.placeholder.green{border-color:#c9df8f}
.body-text{font-size:7.6px;line-height:1.25;color:var(--grey);text-align:justify}
.body-text b{color:var(--ink)}

/* portrait slide */
.content-title{position:absolute;left:62px;top:74px;width:123px;font-size:14px;color:var(--blue);border-bottom:1px solid var(--blue-light);padding-bottom:1px}
.step{position:absolute;left:22px;width:24px;height:24px;border-radius:50%;color:#fff;font-size:12px;display:flex;align-items:center;justify-content:center;border:2px solid #dfe7f2}
.step.one{background:var(--blue-light);top:97px}
.step.two{background:var(--green);top:223px;border-color:#e8f1d2}
.list{position:absolute;left:72px;list-style:none;font-size:9px;color:var(--ink)}
.list li{height:23px;display:flex;align-items:center}
.list li span{color:var(--blue);margin-right:6px;font-size:9px}

/* tables */
.tbl-title{position:absolute;top:76px;font-size:14px;color:var(--ink);display:flex;align-items:center;gap:6px}
.tbl-title b{font-weight:700}
table{position:absolute;top:93px;width:230px;border-collapse:collapse;font-size:5.6px}
th{background:var(--blue);color:#fff;font-weight:400;font-size:8px;height:20px;border-right:1px solid #fff}
td{height:22.4px;color:var(--grey);padding:0 3px;vertical-align:middle}
td.c{text-align:center}
td.i{text-align:center;font-size:8px;color:var(--blue-light)}
.light tr:nth-child(even) td{background:#f3f5f8}
.light tr:nth-child(odd) td{background:#fff}
.light td{border-bottom:1px solid #eef1f5}
.dark th{background:var(--blue-dark)}
.dark td{background:#e4e8ee;color:var(--blue);border:1px solid #9db7d6}
.dark td.i{color:var(--ink)}
.tbl-note{position:absolute;top:315px;width:230px;height:23px;font-size:8.5px;display:flex;align-items:center;justify-content:center}
.tbl-note.light-n{background:var(--green);color:#fff}
.tbl-note.dark-n{background:var(--green-pale);color:var(--ink)}
</style>
</head>
<body>

<!-- Cover, colour -->
<section class="slide s1">
  <div class="abs center wordmark" style="top:125px;font-size:60px;color:#2b2b2b">Vorbelle</div>
  <div class="abs center slogan" style="top:245px">Catalyst for innovation</div>
</section>

<!-- Cover, grey -->
<section class="slide s2">
  <div class="abs center wordmark" style="top:128px;font-size:60px;color:var(--logo-grey)">Vorbelle</div>
  <div class="abs center slogan" style="top:245px">Catalyst for innovation</div>
</section>

<!-- Title slide -->
<section class="slide s3">
  <div class="abs center wordmark" style="top:60px;font-size:52px;color:var(--logo-grey)">Vorbelle</div>
  <div class="abs center" style="top:185px;font-size:41px;color:var(--blue-light);letter-spacing:1px">PRESENTATION TITLE</div>
  <div class="abs center" style="top:229px;font-size:18px;color:var(--ink)">Presentation Subtitle</div>
  <div class="abs center" style="top:281px;font-size:14px;font-style:italic;font-weight:300;color:var(--blue-light)">Name of Presenter</div>
  <div class="abs center" style="top:299px;font-size:14px;font-style:italic;font-weight:300;color:var(--blue-light)">Presenter Title</div>
  <div class="abs center" style="top:317px;font-size:12px;font-style:italic;color:var(--ink)">May 2015</div>
  <div class="abs" style="left:198px;top:340px;width:120px;height:1px;background:var(--blue-light)"></div>
</section>

<!-- Landscape image -->
<section class="slide s4">
  <header class="head"><h2>IMAGE IN LANDSCAPE VIEW</h2><p>With completely <b>customizable</b> icons</p></header>
  <div class="placeholder green" role="img" aria-label="Landscape image area" style="left:34px;top:70px;width:505px;height:198px;width:446px"></div>
  <svg class="abs" style="left:34px;top:287px" width="20" height="16" viewBox="0 0 20 16">
    <rect x="1" y="1" width="18" height="10" rx="1" fill="none" stroke="#9bcb3b" stroke-width="2"/>
    <rect x="8" y="11" width="4" height="3" fill="#9bcb3b"/><rect x="5" y="14" width="10" height="1.5" fill="#9bcb3b"/>
  </svg>
  <p class="abs body-text" style="left:59px;top:287px;width:440px"><b>Aenean</b> ridiculus tortor quis interdum id habitant ad, natoque consectetuer nisl auctor libero quisque euismod ante inceptos malesuada ligula mattis.</p>
  <svg class="abs" style="left:34px;top:316px" width="22" height="16" viewBox="0 0 22 16">
    <polyline points="1,14 8,7 12,11 20,3" fill="none" stroke="#9bcb3b" stroke-width="2.5"/>
    <polygon points="14,2 21,1 20,8" fill="#9bcb3b"/>
  </svg>
  <p class="abs body-text" style="left:59px;top:318px;width:440px"><b>Aenean</b> ridiculus tortor quis interdum id habitant ad, natoque consectetuer nisl auctor libero quisque euismod ante inceptos malesuada ligula mattis.</p>
  <footer class="foot"><span class="mark">Vorbelle</span><span class="line">Catalyst for innovation | <b>PRESENTATION NAME</b></span><span class="num">4</span></footer>
</section>

<!-- Portrait image -->
<section class="slide s5">
  <header class="head muted"><h2>IMAGE IN PORTRAIT VIEW</h2><p>With an example of different typography</p></header>
  <div class="content-title">Content title</div>
  <div class="step one">1</div>
  <p class="abs body-text" style="left:55px;top:99px;width:200px"><b>Aenean</b> ridiculus tortor quis interdum id habitant ad, natoque consectetuer nisl auctor libero quisque euismod ante inceptos malesuada ligula mattis.</p>
  <ul class="list" style="top:146px"><li><span>✓</span>Pellentesque</li><li><span>✓</span>Parturient</li><li><span>✓</span>Ridiculus</li></ul>
  <div class="step two">2</div>
  <p class="abs body-text" style="left:55px;top:225px;width:200px"><b>Aenean</b> ridiculus tortor quis interdum id habitant ad, natoque consectetuer nisl auctor libero quisque euismod ante inceptos malesuada ligula mattis.</p>
  <ul class="list" style="top:272px"><li><span>➡</span>Malesuada</li><li><span>➡</span>Consectetuer</li><li><span>➡</span>Natoque</li></ul>
  <div class="placeholder" role="img" aria-label="Portrait image area" style="left:267px;top:65px;width:219px;height:275px"></div>
  <footer class="foot blue"><span class="mark">Vorbelle</span><span class="line">Catalyst for innovation | <b>PRESENTATION NAME</b></span><span class="num">5</span></footer>
</section>

<!-- Tables -->
<section class="slide s6">
  <header class="head"><h2>COLOR STYLE TABLES</h2><p>Choose from a <b>light</b> or <b>dark</b> theme</p></header>

  <div class="tbl-title" style="left:21px">
    <svg width="16" height="13" viewBox="0 0 16 13"><rect x="1" y="1" width="14" height="11" fill="none" stroke="#3276b5" stroke-width="1.5"/><path d="M1 4.5H15M1 8H15M5.5 1V12M10.5 1V12" stroke="#3276b5" stroke-width="1.2"/></svg>
    <b>Light</b> Theme</div>
  <table class="light" style="left:19px">
    <tr><th style="width:30px">Item</th><th style="width:85px">Step/Action</th><th style="width:60px">Responsible</th><th>Target Date</th></tr>
    <tr><td class="i">1</td><td>Business X, Y, Z high level needs</td><td>Business X, Y, Z</td><td class="c">5/24/2013</td></tr>
    <tr><td class="i">2</td><td>Understand current situation and safety mana</td><td>Business X, Y, Z</td><td class="c">5/31/2013</td></tr>
    <tr><td class="i">3</td><td>Submit Proposal</td><td>Business X, Y, Z</td><td class="c">6/3/2013</td></tr>
    <tr><td class="i">4</td><td>Review Proposal</td><td>Business X, Y, Z</td><td class="c">TBD</td></tr>
    <tr><td class="i">5</td><td>Prepare Final Proposal &amp; Statement of Work (SOW)</td><td>Business X, Y, Z</td><td class="c">TBD</td></tr>
    <tr><td class="i">6</td><td>Complete and sign SOW</td><td>Business X, Y, Z</td><td class="c">TBD</td></tr>
    <tr><td class="i">7</td><td>Schedule project start date</td><td>Business X, Y, Z</td><td class="c">TBD</td></tr>
    <tr><td class="i">8</td><td>Kick-off Project</td><td>Business X, Y, Z</td><td class="c">TBD</td></tr>
    <tr><td class="i">9</td><td>Complete Project</td><td>Business X, Y, Z</td><td class="c">TBD</td></tr>
  </table>
  <div class="tbl-note light-n" style="left:19px">* Additional Information</div>

  <div class="tbl-title" style="left:269px">
    <svg width="16" height="13" viewBox="0 0 16 13"><rect x="1" y="1" width="14" height="11" fill="none" stroke="#0255a3" stroke-width="1.5"/><path d="M1 4.5H15M1 8H15M5.5 1V12M10.5 1V12" stroke="#0255a3" stroke-width="1.2"/></svg>
    <b>Dark</b> Theme</div>
  <table class="dark" style="left:267px">
    <tr><th style="width:30px">Item</th><th style="width:85px">Step/Action</th><th style="width:60px">Responsible</th><th>Target Date</th></tr>
    <tr><td class="i">1</td><td>Business X, Y, Z high level needs</td><td>Business X, Y, Z</td><td class="c">5/24/2013</td></tr>
    <tr><td class="i">2</td><td>Understand current situation and safety mana</td><td>Business X, Y, Z</td><td class="c">5/31/2013</td></tr>
    <tr><td class="i">3</td><td>Submit Proposal</td><td>Business X, Y, Z</td><td class="c">6/3/2013</td></tr>
    <tr><td class="i">4</td><td>Review Proposal</td><td>Business X, Y, Z</td><td class="c">TBD</td></tr>
    <tr><td class="i">5</td><td>Prepare Final Proposal &amp; Statement of Work (SOW)</td><td>Business X, Y, Z</td><td class="c">TBD</td></tr>
    <tr><td class="i">6</td><td>Complete and sign SOW</td><td>Business X, Y, Z</td><td class="c">TBD</td></tr>
    <tr><td class="i">7</td><td>Schedule project start date</td><td>Business X, Y, Z</td><td class="c">TBD</td></tr>
    <tr><td class="i">8</td><td>Kick-off Project</td><td>Business X, Y, Z</td><td class="c">TBD</td></tr>
    <tr><td class="i">9</td><td>Complete Project</td><td>Business X, Y, Z</td><td class="c">TBD</td></tr>
  </table>
  <div class="tbl-note dark-n" style="left:267px">* Additional Information</div>

  <footer class="foot"><span class="mark">Vorbelle</span><span class="line">Catalyst for innovation | <b>PRESENTATION NAME</b></span><span class="num">6</span></footer>
</section>

</body>
</html>
```